Energy trading company (Voltrisa) needs a business card

We need a business card for a company based in Central America. Our main purpose is trading energy . We already have the logo but we need some good creativity to design a high impact business card. Colors blue, orange, green can be used or we would like to see good combinatios with our logo

Target Market(s)

Energy

Industry/Entity Type

Power Generation

Contact Information for Business Card

Logo , headquarters , name, background

Font styles to use
Serif
Sans Serif

Colors

Designer to choose colors to be used in the design.

Requirements
Must have
• it must have a fresh and clean view
Nice to have
• good backgrounds that combine with the logo
Should not have
• too much words

```html
<!DOCTYPE html>
<html lang="en">
<head>
<meta charset="utf-8">
<title>Voltrisa Business Card</title>
<link rel="stylesheet" href="https://fonts.googleapis.com/css2?family=Montserrat:wght@500;700&display=swap">
<style>
  :root {
    --backdrop: #2a176c;
    --card-orange: #e57817;
    --accent-arc: #f3a04e;
    --leaf-green: #5cb450;
    --leaf-green-deep: #2a9d3c;
    --ink-white: #ffffff;
  }
  html, body {
    margin: 0;
    padding: 0;
    width: 1200px;
    height: 1009px;
    overflow: hidden;
    background: var(--backdrop);
  }
  .canvas {
    position: relative;
    width: 1200px;
    height: 1009px;
    background: var(--backdrop);
  }
  .business-card {
    position: absolute;
    left: 69px;
    top: 200px;
    width: 1049px;
    height: 598px;
    background: var(--card-orange);
    overflow: hidden;
  }
  .card-art {
    position: absolute;
    inset: 0;
    width: 100%;
    height: 100%;
  }
  .brand-name {
    position: absolute;
    left: 0;
    width: 1566px;
    top: 245px;
    margin: 0;
    text-align: center;
    font-family: "Montserrat", sans-serif;
    font-weight: 500;
    font-size: 68px;
    line-height: 1;
    letter-spacing: 2px;
    color: var(--ink-white);
  }
  .contact-block {
    position: absolute;
    left: 45px;
    top: 414px;
    font-family: "Montserrat", sans-serif;
    font-weight: 700;
    font-size: 26px;
    line-height: 44px;
    color: var(--ink-white);
  }
  .contact-block p { margin: 0; }
</style>
</head>
<body>
<main class="canvas">
  <section class="business-card">
    <svg class="card-art" viewBox="0 0 1049 598" preserveAspectRatio="none" aria-hidden="true">
      <path class="green-wave-top-edge" fill="var(--leaf-green-deep)"
            d="M0 0 H745 C645 45 565 115 475 178 C385 240 300 262 228 258 C115 252 25 190 0 30 Z"/>
      <path class="green-wave-top" fill="var(--leaf-green)"
            d="M0 0 H740 C640 40 560 108 470 168 C380 228 300 248 230 244 C125 240 35 180 0 18 Z"/>
      <path class="green-wave-bottom-edge" fill="var(--leaf-green-deep)"
            d="M1049 240 C1040 360 1000 450 940 505 C880 560 800 575 700 568 C600 560 500 540 430 560 C400 570 370 585 359 598 H1049 Z"/>
      <path class="green-wave-bottom" fill="var(--leaf-green)"
            d="M1049 262 C1042 375 1005 462 948 516 C888 572 800 586 700 580 C600 574 505 556 440 572 C415 579 395 590 385 598 H1049 Z"/>
      <path class="accent-arc" fill="none" stroke="var(--accent-arc)" stroke-width="3"
            d="M571 98 C520 160 500 260 515 340 C540 460 660 540 800 535 C850 533 880 520 906 510"/>
    </svg>
    <h1 class="brand-name">Voltrisa</h1>
    <div class="contact-block">
      <p class="contact-name">Name</p>
      <p class="contact-headquarters">Headquarters</p>
    </div>
  </section>
</main>
</body>
</html>
```